Meridel Bidding Group Website

We are an food equipment auction company and are in need of an updated website. Old website found here: http://meridelbiddinggroup.example/ . We need to be able to share upcoming auctions, past auctions, companies we've worked with, needs to be mobile friendly. We will also need an easy to access back office where we can add new info, auction info, etc.

Target Market(s)

Equipment auctions, large food manufacturers, equipment resalers

Industry/Entity Type

Auction

Coding

Number of Pages Required

5+ page

Font styles to use
Sans Serif

Colors
acd136
ffffff

Requirements
Must have
• Back office where we can add new auctions
-mobile friendly
-contact us page,
-services page
-social media widgets
-must match our current logo
-current auctions on front page
- join mailing list
- past auctions / current auctions pages
Nice to have
• Would like it to be clean design, easy to view and find options, modern

```html
<!DOCTYPE html>
<html lang="en">
<head>
<meta charset="utf-8">
<title>Meridel Bidding Group</title>
<link href="https://fonts.googleapis.com/css2?family=Roboto:wght@400;500;700&family=Rubik:wght@500;700&display=swap" rel="stylesheet">
<style>
:root{
  --green:#8dc63f;
  --green-dark:#7ab22f;
  --slate:#58595b;
  --slate-dark:#4a4b4d;
  --ink:#222;
  --text:#555;
  --light:#f1f1f1;
  --white:#fff;
}
*{margin:0;padding:0;box-sizing:border-box}
html,body{width:1200px;height:3675px;overflow:hidden}
body{font-family:"Roboto",Arial,sans-serif;color:var(--ink);background:var(--white);position:relative}
.abs{position:absolute}
.heading{font-family:"Rubik","Roboto",sans-serif;font-weight:700;text-transform:uppercase}
.btn{position:absolute;background:var(--green);color:var(--white);border-radius:24px;font-weight:700;font-size:15px;text-transform:uppercase;display:flex;align-items:center;justify-content:center;gap:8px}
.btn .dot{width:15px;height:15px;border-radius:50%;background:var(--white);position:relative}
.btn .dot::after{content:"";position:absolute;left:4px;top:4px;border-left:6px solid var(--green);border-top:3.5px solid transparent;border-bottom:3.5px solid transparent}

/* header */
.topbar{left:360px;top:0;width:840px;height:46px;background:var(--slate);clip-path:polygon(28px 0,100% 0,100% 100%,0 100%)}
.topbar-line{left:330px;top:44px;width:870px;height:4px;background:var(--green)}
.topbar-text{top:14px;font-size:12px;color:var(--white)}
.social-mini{top:12px;width:20px;height:20px;border-radius:50%;background:var(--slate-dark);border:1px solid #777}
.brand{left:111px;top:30px;display:flex;align-items:center;gap:12px}
.brand-square{width:60px;height:60px;background:var(--green)}
.brand-name{font-family:"Rubik",sans-serif;font-weight:700;font-size:20px;line-height:22px;color:var(--slate);text-transform:uppercase}
.nav{top:71px;font-size:15px;font-weight:500;color:var(--ink)}
.nav.active{color:var(--green)}

/* hero */
.hero{left:0;top:113px;width:1200px;height:662px;background:linear-gradient(100deg,#8e8e88 0%,#6f706b 35%,#55554f 70%,#6b6b66 100%)}
.hero-title{left:111px;top:290px;color:var(--white);font-size:46px;line-height:47px}
.hero-sub{left:111px;top:404px;width:500px;color:var(--white);font-size:17px;line-height:26px}
.circle-arrow{width:88px;height:88px;border-radius:50%;background:var(--white);border:3px solid #ddd;box-shadow:0 0 0 6px rgba(255,255,255,.4)}

/* welcome */
.welcome-img{left:108px;top:858px;width:450px;height:364px;background:linear-gradient(135deg,#8dc63f,#9ea39a 55%,#6a6c67);clip-path:polygon(25% 0,75% 0,100% 50%,75% 100%,25% 100%,0 50%)}
.eyebrow{color:var(--green);font-family:"Rubik",sans-serif;font-weight:500;font-size:19px}
.welcome-title{left:630px;top:900px;font-size:33px;color:var(--slate)}
.welcome-copy{left:631px;top:956px;width:470px;font-size:14px;line-height:25px;color:var(--text)}

/* auctions */
.auctions-band{left:0;top:1290px;width:1200px;height:935px}
.section-title{width:1200px;text-align:center;font-size:38px}
.tab{top:1551px;height:41px;width:200px;border-radius:22px;font-size:15px;font-weight:500;display:flex;align-items:center;justify-content:center;text-transform:uppercase}
.card{top:1650px;width:309px;height:415px;background:var(--white);border-radius:10px;box-shadow:0 4px 12px rgba(0,0,0,.2)}
.card-img{position:absolute;left:7px;top:7px;width:295px;height:195px}
.card-title{position:absolute;left:10px;top:226px;width:289px;text-align:center;font-size:16px;font-weight:700;line-height:24px}
.card-meta{position:absolute;left:0;top:290px;width:309px;text-align:center;font-size:12px;color:#333}
.card-loc{position:absolute;left:0;top:314px;width:309px;text-align:center;font-size:13px;font-weight:500}
.ico-g{color:var(--green)}
.card .btn{left:82px;top:356px;width:146px;height:38px;font-size:15px;font-weight:500}
.chev{top:1838px;width:20px;height:38px}

/* services */
.svc-label{font-size:17px;font-weight:500;color:var(--ink)}
.svc-icon{width:68px;height:68px;border-radius:50%}
.svc-icon.g{background:var(--green)}
.svc-icon.s{background:var(--slate)}

/* clients */
.clients{left:0;top:2827px;width:1200px;height:400px;background:var(--light)}
.client{top:2977px;width:165px;height:86px;background:var(--white);border-radius:4px;box-shadow:0 2px 8px rgba(0,0,0,.15);display:flex;align-items:center;justify-content:center;font-size:12px;font-weight:700;color:var(--slate);text-transform:uppercase;letter-spacing:.5px;text-align:center}

/* footer */
.foot-h{font-size:17px;font-weight:700;color:var(--white);text-transform:uppercase}
.field{height:38px;background:var(--white);font-size:12px;color:#555;padding:14px 0 0 18px}
.link{font-size:14px;color:var(--white)}
.link::before{content:"»";color:var(--green);margin-right:12px}
.contact{font-size:14px;color:var(--white);line-height:24px}
.social{top:3521px;width:32px;height:32px;border-radius:50%;background:var(--white)}
</style>
</head>
<body>

<!-- header -->
<div class="abs topbar"></div>
<div class="abs topbar-line"></div>
<div class="abs topbar-text" style="left:413px">Leaders In Food Manufacturing And Packaging Equipment Auctions</div>
<div class="abs topbar-text" style="left:855px">&#9990; 555 014 2290</div>
<div class="abs social-mini" style="left:1001px" aria-label="Social profile"></div>
<div class="abs social-mini" style="left:1034px" aria-label="Social profile"></div>
<div class="abs social-mini" style="left:1067px" aria-label="Social profile"></div>
<div class="abs brand"><div class="brand-square"></div><div class="brand-name">Meridel<br>Bidding Group</div></div>
<div class="abs nav active" style="left:434px">Home</div>
<div class="abs nav" style="left:506px">Services</div>
<div class="abs nav" style="left:595px">Auctions</div>
<div class="abs nav" style="left:688px">Equipment Finder</div>
<div class="abs nav" style="left:840px">Resources</div>
<div class="abs nav" style="left:943px">FAQ's</div>
<div class="abs nav" style="left:1011px">Contact Us</div>

<!-- hero -->
<div class="abs hero" role="img" aria-label="Photo of stainless steel food production line in a factory"></div>
<svg class="abs" style="left:0;top:660px" width="1200" height="182" viewBox="0 0 1200 182">
  <polygon points="0,115 1200,5 1200,182" fill="var(--green)"/>
  <polygon points="0,115 1200,5 1200,0 0,0" fill="none"/>
  <polygon points="0,115 0,182 1200,182" fill="var(--white)"/>
</svg>
<h1 class="abs heading hero-title">Meridel<br>Bidding Group</h1>
<p class="abs hero-sub">Meridel Bidding Group is a full-service asset-management company specializing in food manufacturing</p>
<div class="btn" style="left:111px;top:481px;width:193px;height:46px">Get Started <span class="dot"></span></div>
<div class="abs circle-arrow" style="left:556px;top:673px">
  <svg width="82" height="82" viewBox="0 0 82 82"><path d="M29 33l12 11 12-11M29 42l12 11 12-11" stroke="#666" stroke-width="2.5" fill="none"/></svg>
</div>

<!-- welcome -->
<div class="abs welcome-img" role="img" aria-label="Hexagon collage of factory equipment photos"></div>
<div class="abs eyebrow" style="left:631px;top:876px">Welcome To</div>
<h2 class="abs heading welcome-title">Meridel Bidding Group</h2>
<p class="abs welcome-copy">Meridel Bidding Group is a full-service asset-management company specializing in food manufacturing and packaging equipment. Our goal at Meridel Bidding Group is to provide our customers with a range of options to liquidate their assets. A few of the services we offer are appraisals, asset management, live onsite auctions, online auctions and orderly negotiated sales. We help our customers determine the best options to maximize returns within their given parameters.</p>
<div class="btn" style="left:631px;top:1160px;width:160px;height:43px">Learn More <span class="dot"></span></div>

<!-- auctions -->
<svg class="abs auctions-band" width="1200" height="935" viewBox="0 0 1200 935">
  <polygon points="0,0 560,125 0,177" fill="var(--slate)"/>
  <polygon points="0,177 560,125 1200,70 1200,855 0,935" fill="var(--green)"/>
</svg>
<div class="abs" style="left:0;top:1390px;width:1200px;height:800px;background:linear-gradient(180deg,rgba(255,255,255,.05),rgba(0,0,0,.06))" role="img" aria-label="Faded factory floor photo tinted green"></div>
<h2 class="abs heading section-title" style="left:0;top:1487px;color:var(--white)">Our Auctions</h2>
<div class="abs tab" style="left:389px;background:var(--white);color:var(--green)">Upcoming Auctions</div>
<div class="abs" style="left:482px;top:1590px;border-left:7px solid transparent;border-right:7px solid transparent;border-top:7px solid var(--white)"></div>
<div class="abs tab" style="left:612px;background:var(--slate);color:var(--white)">Past Auctions</div>

<svg class="abs chev" style="left:43px" viewBox="0 0 20 38"><path d="M17 3L3 19l14 16" stroke="#fff" stroke-width="4" fill="none"/></svg>
<svg class="abs chev" style="left:1134px" viewBox="0 0 20 38"><path d="M3 3l14 16L3 35" stroke="#fff" stroke-width="4" fill="none"/></svg>

<div class="abs card" style="left:111px">
  <div class="card-img" role="img" aria-label="Photo of packaging conveyors with blue belts" style="background:linear-gradient(160deg,#8a8f96,#4d6a9c 60%,#2f56a8)"></div>
  <div class="card-title">Surplus Assets to National Premium Dessert Supplier</div>
  <div class="card-meta"><span class="ico-g">&#9635;</span> 1/20/2021 &nbsp;&nbsp;|&nbsp;&nbsp; <span class="ico-g">&#9719;</span> 10:00 AM</div>
  <div class="card-loc"><span class="ico-g">&#9679;</span> Multi Location California &amp; , CO</div>
  <div class="btn">View Details</div>
</div>
<div class="abs card" style="left:445px">
  <div class="card-img" role="img" aria-label="Photo of long candy cooling conveyor line" style="background:linear-gradient(160deg,#b9b7b2,#8a4a2a 50%,#7c7b78)"></div>
  <div class="card-title">Large Candy &amp; Confections Surplus Equipment Auction</div>
  <div class="card-meta"><span class="ico-g">&#9635;</span> 1/7/2021 &nbsp;&nbsp;|&nbsp;&nbsp; <span class="ico-g">&#9719;</span> 10:00 AM</div>
  <div class="card-loc"><span class="ico-g">&#9679;</span> Montrose, CO</div>
  <div class="btn">View Details</div>
</div>
<div class="abs card" style="left:778px">
  <div class="card-img" role="img" aria-label="Photo of meat processing room with steel tables" style="background:linear-gradient(160deg,#cfd0cc,#8d8f8c 55%,#5e605d)"></div>
  <div class="card-title">Producer of links, patties, hot dogs, steaks &amp; more!</div>
  <div class="card-meta"><span class="ico-g">&#9635;</span> 12/3/2020 &nbsp;&nbsp;|&nbsp;&nbsp; <span class="ico-g">&#9719;</span> 10:00 AM</div>
  <div class="card-loc"><span class="ico-g">&#9679;</span> Cedar Rapids, IA</div>
  <div class="btn">View Details</div>
</div>

<!-- services -->
<h2 class="abs heading section-title" style="left:0;top:2268px;color:var(--slate)"><span style="color:var(--green)">Our</span> Services</h2>
<p class="abs" style="left:0;top:2320px;width:1200px;text-align:center;font-size:14px;color:var(--text)">Below are a list of our services please contact us for more information.</p>

<svg class="abs" style="left:0;top:2380px" width="1200" height="400" viewBox="0 0 1200 400">
  <g stroke="#bbb" stroke-width="1.5" fill="none">
    <path d="M420 42h22l50 34"/><path d="M780 42h-22l-50 34"/>
    <path d="M389 188h55"/><path d="M811 188h-55"/>
    <path d="M420 335h22l50-34"/><path d="M780 335h-22l-50-34"/>
  </g>
  <circle cx="600" cy="190" r="157" fill="none" stroke="var(--slate)" stroke-width="4"/>
  <circle cx="600" cy="190" r="128" fill="var(--white)" stroke="#eee" stroke-width="8"/>
  <g fill="var(--white)" stroke="var(--green)" stroke-width="4">
    <circle cx="491" cy="76" r="7"/><circle cx="709" cy="76" r="7"/>
    <circle cx="444" cy="190" r="7"/><circle cx="756" cy="190" r="7"/>
    <circle cx="493" cy="302" r="7"/><circle cx="707" cy="302" r="7"/>
  </g>
  <text x="600" y="184" text-anchor="middle" font-family="Rubik, sans-serif" font-weight="700" font-size="24" fill="#58595b">MERIDEL</text>
  <text x="600" y="212" text-anchor="middle" font-family="Rubik, sans-serif" font-weight="700" font-size="17" fill="#58595b">BIDDING GROUP</text>
</svg>
<div class="abs svc-icon g" style="left:352px;top:2388px"></div>
<div class="abs svc-icon s" style="left:321px;top:2534px"></div>
<div class="abs svc-icon g" style="left:352px;top:2681px"></div>
<div class="abs svc-icon s" style="left:780px;top:2388px"></div>
<div class="abs svc-icon g" style="left:811px;top:2534px"></div>
<div class="abs svc-icon s" style="left:780px;top:2681px"></div>
<div class="abs svc-label" style="left:133px;top:2411px">Orderly Negotiated Sales</div>
<div class="abs svc-label" style="left:209px;top:2557px">Real Estate</div>
<div class="abs svc-label" style="left:176px;top:2704px">Turnkey Operations</div>
<div class="abs svc-label" style="left:871px;top:2411px">Appraisals</div>
<div class="abs svc-label" style="left:901px;top:2557px">Asset Management</div>
<div class="abs svc-label" style="left:869px;top:2704px">Auctions</div>

<!-- clients -->
<div class="abs clients"></div>
<div class="abs" style="left:0;top:2872px;width:1200px;text-align:center;color:var(--green);font-size:16px;font-weight:500">OUR CLIENTS</div>
<h2 class="abs heading section-title" style="left:0;top:2893px;color:var(--slate);font-size:37px">We Work With Us</h2>
<div class="abs client" style="left:120px">Hearthline Homes</div>
<div class="abs client" style="left:319px">Trivex Studio</div>
<div class="abs client" style="left:518px">Glowpoint</div>
<div class="abs client" style="left:716px">Banfield Supply</div>
<div class="abs client" style="left:915px">Norvale Foods</div>

<!-- footer -->
<svg class="abs" style="left:0;top:3090px" width="1200" height="585" viewBox="0 0 1200 585">
  <rect x="0" y="70" width="1200" height="515" fill="var(--slate)"/>
  <polygon points="0,70 1200,0 1200,70" fill="var(--slate)"/>
  <polygon points="1200,0 640,142 1200,142" fill="var(--green)"/>
</svg>
<div class="abs circle-arrow" style="left:556px;top:3188px">
  <svg width="82" height="82" viewBox="0 0 82 82"><path d="M29 49l12-11 12 11M29 40l12-11 12 11" stroke="#666" stroke-width="2.5" fill="none"/></svg>
</div>

<div class="abs foot-h" style="left:111px;top:3300px">Get In Touch</div>
<div class="abs field" style="left:111px;top:3343px;width:235px">First Name</div>
<div class="abs field" style="left:353px;top:3343px;width:235px">Last Name</div>
<div class="abs field" style="left:111px;top:3392px;width:235px">Email</div>
<div class="abs field" style="left:353px;top:3392px;width:235px">phone number</div>
<div class="abs field" style="left:111px;top:3440px;width:477px;height:72px">Message</div>
<div class="btn" style="left:111px;top:3537px;width:96px;height:32px;font-size:14px;border-radius:16px">Submit</div>

<div class="abs foot-h" style="left:641px;top:3300px">Quick Links</div>
<div class="abs link" style="left:643px;top:3337px">Home</div>
<div class="abs link" style="left:643px;top:3367px">Services</div>
<div class="abs link" style="left:643px;top:3397px">FAQ's</div>
<div class="abs link" style="left:643px;top:3427px">Auctions</div>
<div class="abs link" style="left:643px;top:3457px">Equipment Finder</div>

<div class="abs foot-h" style="left:852px;top:3300px">Contact Us</div>
<div class="abs contact" style="left:856px;top:3344px"><span class="ico-g">&#9679;</span></div>
<div class="abs contact" style="left:883px;top:3344px">Head Office 48 Orchard Yard Lane<br>Fairbrook, ND 50000</div>
<div class="abs contact" style="left:856px;top:3398px"><span class="ico-g">&#9647;</span>&nbsp;&nbsp;&nbsp; (555) 014-3356</div>
<div class="abs contact" style="left:854px;top:3433px"><span class="ico-g">&#9635;</span>&nbsp;&nbsp;&nbsp; +1 555 014 7890</div>
<div class="abs contact" style="left:854px;top:3466px"><span class="ico-g">&#9993;</span>&nbsp;&nbsp; info@meridelbiddinggroup.example</div>

<div class="abs foot-h" style="left:641px;top:3528px">Stay Connected :</div>
<div class="abs social" style="left:841px" aria-label="Social profile"></div>
<div class="abs social" style="left:880px" aria-label="Social profile"></div>
<div class="abs social" style="left:919px" aria-label="Social profile"></div>

<div class="abs" style="left:0;top:3632px;width:1200px;text-align:center;font-size:13px;color:var(--white)">© 2021 Meridel Bidding Group &nbsp;&nbsp;|&nbsp;&nbsp; All Rights Reserved &nbsp;&nbsp;|&nbsp;&nbsp; Terms and Conditions</div>

</body>
</html>
```